We need a business card for our gym. We are a LiftCore affiliate in Decatur Georgie established 2008. Our company name is Tarn Functional Fitness. LiftCore Shaping Peak Fitness. Instagram and website is @tarnhall. Hashtags we use #lifewithgrit #madetolift We want something similar to the the black and neon green design attached but a different color scheme. No neon colors. Are company colors are the same as the blue and white card attached. We are open to ideas as far as colors however - just no neon.

Contact Information for Business Card

Tarn Functional Fitness
427 Pellow Drive
Ashgrove 30817
Phone 404.555.0186 Website www.tarnhall.example

Font styles to use
Other font styles liked:
• Futura Extra Bold Condensed

Colors

Designer to choose colors to be used in the design.

Requirements
Must have
• Our primary font we typically use for our name is Futura Extra Bold Condensed
Nice to have
• I attached a card from that is black and neon green from Vexa that we would like something similar. The blue and white is more similar to our colors. We also use have used black and white in the past. We use the chevrons as out logo. We are a LiftCore affiliate so I included a logo from them as well that may or may not be used on the card. Our instagram is @tarnhall hashtags #madetolift #lifewithgrit
Should not have
• No neon colors

```html
<!DOCTYPE html>
<html lang="en">
<head>
<meta charset="utf-8">
<title>Tarn Functional Fitness – Business Card</title>
<link rel="stylesheet" href="https://fonts.googleapis.com/css2?family=Anton&family=Oswald:wght@500;600&family=Montserrat:wght@300;400;600&display=swap">
<style>
  :root {
    --brand-blue: #2f8fb0;
    --brand-blue-deep: #237894;
    --brand-blue-light: #3a9fc0;
    --paper: #ffffff;
    --ink: #4a4a4a;
    --stage: #e9ecee;
  }
  * { box-sizing: border-box; margin: 0; padding: 0; }
  html, body {
    width: 1200px; height: 900px; overflow: hidden;
    background: var(--stage);
  }
  .sheet { position: relative; width: 1200px; height: 900px; }
  .card {
    position: absolute; left: 250px; width: 700px; height: 400px;
    overflow: hidden;
    box-shadow: 0 6px 18px rgba(0,0,0,.12);
  }

  /* ---------- front ---------- */
  .card-front { top: 35px; background: var(--paper); }
  .front-band {
    position: absolute; left: 0; right: 0; bottom: 0; height: 16px;
    background: var(--brand-blue);
  }
  .brand {
    position: absolute; left: 48px; top: 48px;
    display: flex; align-items: center; gap: 14px;
  }
  .brand-mark { width: 26px; height: 26px; background: var(--brand-blue); flex: none; }
  .brand-name {
    font-family: "Anton", "Oswald", sans-serif;
    font-size: 40px; line-height: 1; text-transform: uppercase;
    letter-spacing: .5px; color: var(--brand-blue); white-space: nowrap;
  }
  .address {
    position: absolute; left: 48px; bottom: 46px;
    font-family: "Montserrat", sans-serif; font-weight: 300;
    font-size: 18px; color: var(--ink);
  }
  .contact { position: absolute; left: 410px; top: 170px; }
  .contact-name {
    font-family: "Oswald", sans-serif; font-weight: 600;
    font-size: 30px; letter-spacing: 1px; text-transform: uppercase;
    color: var(--brand-blue); line-height: 1.05;
  }
  .contact-role {
    font-family: "Montserrat", sans-serif; font-weight: 300;
    font-size: 18px; color: var(--ink); margin-bottom: 10px;
  }
  .contact-list { list-style: none; }
  .contact-list li {
    display: flex; align-items: center; gap: 10px;
    font-family: "Montserrat", sans-serif; font-weight: 300;
    font-size: 17px; color: var(--ink); line-height: 1.55;
  }
  .contact-list svg { width: 16px; height: 16px; flex: none; }

  /* ---------- back ---------- */
  .card-back { top: 465px; background: var(--brand-blue); }
  .back-texture {
    position: absolute; inset: 0;
    background: linear-gradient(135deg, var(--brand-blue-light), var(--brand-blue) 55%, var(--brand-blue-deep));
  }
  .back-brand {
    position: absolute; inset: 0;
    display: flex; align-items: center; justify-content: center;
  }
  .back-brand .brand-name { color: var(--paper); font-size: 44px; }
</style>
</head>
<body>
<main class="sheet">

  <section class="card card-front" aria-label="Card front">
    <div class="brand">
      <span class="brand-mark"></span>
      <span class="brand-name">Tarn Functional Fitness</span>
    </div>

    <div class="contact">
      <h1 class="contact-name">Dana Whitlock</h1>
      <p class="contact-role">President/ CEO</p>
      <ul class="contact-list">
        <li>
          <svg viewBox="0 0 16 16" fill="none" stroke="#2f8fb0" stroke-width="1.3"><circle cx="8" cy="8" r="7"/><path d="M5.5 4.5l1.5 1.5-1 1c.6 1.3 1.7 2.4 3 3l1-1 1.5 1.5-1 1c-2.8-.4-5.6-3.2-6-6z"/></svg>
          404.555.0186
        </li>
        <li>
          <svg viewBox="0 0 16 16" fill="none" stroke="#2f8fb0" stroke-width="1.3"><rect x="1.5" y="3.5" width="13" height="9"/><path d="M1.5 3.5L8 9l6.5-5.5"/></svg>
          info@tarnhall.example
        </li>
        <li>
          <svg viewBox="0 0 16 16" fill="none" stroke="#2f8fb0" stroke-width="1.3"><circle cx="8" cy="8" r="6.5"/><ellipse cx="8" cy="8" rx="3" ry="6.5"/><path d="M1.5 8h13"/></svg>
          www.tarnhall.example
        </li>
      </ul>
    </div>

    <p class="address">427 Pellow Drive, Ashgrove 30817</p>
    <div class="front-band"></div>
  </section>

  <section class="card card-back" aria-label="Card back">
    <div class="back-texture" role="img" aria-label="Tone-on-tone repeating brand pattern across the card back"></div>
    <div class="back-brand">
      <span class="brand-name">Tarn Functional Fitness</span>
    </div>
  </section>

</main>
</body>
</html>
```